Brightway Inc. Business Card Design

Brightway Inc. is in search of a great clean design for our business cards!

Looking to incorporate our full logo and watermark on side one (however, I am open to having the text and watermark separated within the design.)

On side two, I am looking to have contact information (Name, Position, Phone #, Email, Website (www.thebrightway.ca). Can have the logo and/or watermark as part of the design if applicable.

Please add tagline "Where Shine Counts" on either side 1 or 2. This tagline can be in a sans serif, serif or cursive font as long as it compliments overall design. Capitalization can be title or sentence case depending on how it fits within the design.

Get creative!! Looking for a clean, crisp, premium design! Looking for a glossy card finish with spot UV features when printed. Cards will also be printed with rounded corners. Standard dimensions (3.5 x 2).

Target Market(s)

B2B - primary clients are business owners or property management corporations. (residential jobs are few and far between)

Industry/Entity Type

Business

Contact Information for Business Card

- clean, crisp design
- double sided
- spot UV accents and glossy finish upon printing
- standard business card size (3.5 x 2) with rounded corners
- please see project description for requirements per side

Font styles to use
Sans Serif

Requirements
Must have
• - adequate bleeds with print ready files
• - cohesive design elements between side 1 & 2
• - spot UV elements (can be on both sides or just one, use your discretion)
• - colour pallet should match the logo file provided
• - incorporate tagline "where shine counts" (this tagline can be in a serif or sans serif font as long as it is complimentary to the overall design.
Nice to have
• - Premium elements with a clean design
Should not have
• - Please omit cartoon or whimsical like designs, think premium.
• - Colours should not stray from the pallet of the provided logo.

```html
<!DOCTYPE html>
<html lang="en">
<head>
<meta charset="utf-8">
<title>Brightway Inc. Business Card</title>
<link rel="stylesheet" href="https://fonts.googleapis.com/css2?family=Open+Sans:wght@400;600;700&family=Italianno&display=swap">
<style>
  :root {
    --page: #d9d9db;
    --card-dark: #323234;
    --card-light: #f4f4f5;
    --navy: #2b3561;
    --teal: #1fb0b2;
    --ink: #4a4d57;
    --muted: #6f727b;
    --silver: #a9abb0;
    --panel: #e6e6e8;
  }
  * { margin: 0; padding: 0; box-sizing: border-box; }
  html, body { width: 1200px; height: 904px; overflow: hidden; }
  body {
    background: var(--page);
    font-family: "Open Sans", Arial, sans-serif;
    position: relative;
  }
  .card {
    position: absolute;
    left: 250px;
    width: 700px;
    height: 400px;
    border-radius: 14px;
    overflow: hidden;
  }
  .card--back { top: 40px; background: var(--card-dark); }
  .card--front { top: 464px; background: var(--card-light); }

  .wordmark {
    display: flex;
    align-items: center;
    gap: 12px;
    font-weight: 700;
    letter-spacing: 0.5px;
  }
  .wordmark__square { width: 30px; height: 30px; }
  .card--back .wordmark {
    position: absolute; left: 0; right: 0; top: 150px;
    justify-content: center;
    font-size: 40px; color: var(--silver);
  }
  .card--back .wordmark__square { background: var(--silver); }
  .tagline {
    position: absolute; left: 0; right: 0; top: 270px;
    text-align: center;
    font-family: "Italianno", cursive;
    font-size: 40px;
    color: #f2f2f2;
  }

  .watermark-panel { position: absolute; right: 0; top: 0; width: 320px; height: 400px; }

  .card--front .wordmark {
    position: absolute; left: 60px; top: 92px;
    font-size: 38px; color: var(--navy);
  }
  .card--front .wordmark__square { background: var(--teal); width: 32px; height: 32px; }

  .person { position: absolute; left: 100px; top: 168px; }
  .person__name { font-size: 22px; font-weight: 700; color: var(--navy); }
  .person__role { font-size: 15px; color: var(--muted); margin-top: 2px; margin-left: 14px; }

  .address {
    position: absolute; left: 128px; top: 232px;
    font-size: 15px; line-height: 21px; color: var(--ink);
  }
  .contacts {
    position: absolute; left: 112px; top: 284px;
    list-style: none;
    font-size: 15px; color: var(--ink);
  }
  .contacts li { display: flex; align-items: center; gap: 14px; height: 24px; }
  .contacts svg { width: 14px; height: 14px; flex: none; }
</style>
</head>
<body>
  <section class="card card--back" aria-label="Card back">
    <div class="wordmark"><span class="wordmark__square"></span><span>BRIGHTWAY</span></div>
    <p class="tagline">where shine counts</p>
  </section>

  <section class="card card--front" aria-label="Card front">
    <svg class="watermark-panel" viewBox="0 0 320 400" role="img" aria-label="Faint large brand watermark area">
      <defs>
        <linearGradient id="panelTone" x1="0" y1="0" x2="1" y2="1">
          <stop offset="0" stop-color="#ececee"/>
          <stop offset="1" stop-color="#dcdcdf"/>
        </linearGradient>
      </defs>
      <polygon points="40,0 320,0 320,400 80,400 20,260" fill="url(#panelTone)"/>
    </svg>

    <div class="wordmark"><span class="wordmark__square"></span><span>BRIGHTWAY</span></div>

    <div class="person">
      <p class="person__name">Daniel Reyes</p>
      <p class="person__role">Manager</p>
    </div>

    <p class="address">24 Harbour Lane, Suite 5<br>Westfield, ON L4K 2B7.</p>

    <ul class="contacts">
      <li>
        <svg viewBox="0 0 14 14" aria-hidden="true"><circle cx="7" cy="7" r="7" fill="var(--teal)"/><path d="M4.5 3.8l1.4 0 .5 1.8-.8.7a5 5 0 0 0 2.1 2.1l.7-.8 1.8.5v1.4c-3.5.2-6-2.4-5.7-5.7z" fill="#fff"/></svg>
        <span>+1 905 555 0148</span>
      </li>
      <li>
        <svg viewBox="0 0 14 14" aria-hidden="true"><circle cx="7" cy="7" r="7" fill="var(--teal)"/><rect x="3.5" y="4.5" width="7" height="5" fill="#fff"/><path d="M3.5 4.5l3.5 2.8 3.5-2.8" stroke="var(--teal)" stroke-width="0.8" fill="none"/></svg>
        <span>info@thebrightway.ca</span>
      </li>
      <li>
        <svg viewBox="0 0 14 14" aria-hidden="true"><circle cx="7" cy="7" r="7" fill="var(--teal)"/><circle cx="7" cy="7" r="3.6" stroke="#fff" stroke-width="0.9" fill="none"/><path d="M3.4 7h7.2M7 3.4c-1.6 2-1.6 5.2 0 7.2M7 3.4c1.6 2 1.6 5.2 0 7.2" stroke="#fff" stroke-width="0.8" fill="none"/></svg>
        <span>www.thebrightway.ca</span>
      </li>
    </ul>
  </section>
</body>
</html>
```